Weight Loss Banner Ad

We need banner ads for our website, www.brightplatekitchen.com. We would like to see Banner ads that represent what you think is the most captivating aspect of The MealWise Plan. Please review the website.

The banner ad should be something you REALLY want to click on. It needs to include the name and/or logo and the slogan "Gourmet Meals Direct To Your House"

We will want the final ad in multiple sizes but it should use the same image and copy.

Logo is attached, so are images. Feel free to use your own if you think you have a better on

Size (pixels):
468 x 60
392 x 72
234 x 60
125 x 125
120 x 90
120 x 60
88 x 31
120 x 240
120 x 600
160 x 600

Target Market(s)

Fitness Enthusiast looking to lose weight.

Industry/Entity Type

Weight

Font styles to use
Sans Serif

Requirements
Must have
• See Description
Nice to have
• Should be awesome and make you want to buy some food. Also you may want to say something about the price:

i.e. Starting at only $99

```html
<!DOCTYPE html>
<html lang="en">
<head>
<meta charset="utf-8">
<title>The MealWise Plan – Banner Set</title>
<link rel="stylesheet" href="https://fonts.googleapis.com/css2?family=Lato:wght@400;700;900&display=swap">
<style>
  :root {
    --page: #ffffff;
    --panel: #3d3d3d;
    --panel-edge: #555555;
    --headline: #c6df8e;
    --brand-green: #8cc63f;
    --ribbon-light: #cfe5a4;
    --ribbon-dark: #7db730;
    --badge-outer: #5a5a5a;
    --badge-inner: #4a4a4a;
    --ink: #1e1e1e;
    --white: #ffffff;
    --label-red: #e0241b;
    --btn-top: #9ad63c;
    --btn-bottom: #3f8a10;
  }
  * { box-sizing: border-box; margin: 0; padding: 0; }
  html, body { width: 1200px; height: 1157px; overflow: hidden; background: var(--page); }
  .stage {
    position: relative; width: 700px; height: 675px;
    transform: scale(1.7142857); transform-origin: 0 0;
    font-family: "Lato", Arial, sans-serif;
  }
  .banner { position: absolute; background: var(--panel); border: 1px solid var(--panel-edge); overflow: hidden; }
  .banner--tall { width: 160px; height: 602px; }
  .banner--wide { width: 301px; height: 250px; }

  .media-panel { position: absolute; background: var(--white); overflow: hidden; }
  .media-panel::before {
    content: ""; position: absolute; left: 50%; top: 0; width: 16px; height: 9px;
    transform: translateX(-50%); background: var(--panel);
    clip-path: polygon(0 0, 100% 0, 50% 100%);
  }
  .brand-name {
    position: absolute; left: 0; right: 0; text-align: center;
    color: var(--brand-green); font-weight: 900; line-height: 1;
  }
  .photo { position: absolute; left: 0; right: 0; bottom: 0; }
  .photo--salad { background: linear-gradient(160deg, #f2f2f0 0%, #e4d6cb 40%, #c9a896 55%, #eef1ea 75%, #9fc46a 100%); }
  .photo--waist { background: linear-gradient(170deg, #eaf1df 0%, #d9b79e 35%, #c99a7f 60%, #3a3a3a 85%, #e6efd8 100%); }

  .headline { position: absolute; text-align: center; color: var(--headline); font-weight: 900; text-transform: uppercase; }
  .banner--tall .headline { left: 8px; right: 8px; top: 232px; font-size: 17px; line-height: 22px; }
  .slogan { position: absolute; text-align: center; color: var(--white); font-weight: 400; }
  .banner--tall .slogan { left: 0; right: 0; top: 324px; font-size: 13.5px; line-height: 18px; }

  .price-badge { position: absolute; border-radius: 50%; background: radial-gradient(circle, var(--badge-inner) 0 62%, var(--badge-outer) 63% 100%); }
  .ribbon { position: absolute; text-align: center; }
  .ribbon__intro { background: var(--ribbon-light); color: var(--ink); font-weight: 400; text-transform: uppercase; display: flex; align-items: center; justify-content: center; }
  .ribbon__price { background: var(--ribbon-dark); color: #111; font-weight: 400; display: flex; justify-content: center; clip-path: polygon(0 0, 100% 0, 100% 100%, 50% 86%, 0 100%); }

  .cta {
    position: absolute; display: flex; align-items: center; justify-content: center; gap: 8px;
    border-radius: 4px; background: linear-gradient(var(--btn-top), var(--btn-bottom));
    color: var(--white); font-weight: 900; text-transform: uppercase; letter-spacing: .2px;
    text-shadow: 0 1px 1px rgba(0,0,0,.35); box-shadow: inset 0 1px 0 rgba(255,255,255,.5);
  }
  .cta svg { flex: none; }
  .site-url { position: absolute; text-align: center; font-weight: 400; }
  .banner--tall .site-url { left: 0; right: 0; bottom: 0; height: 27px; line-height: 27px; background: var(--white); color: var(--ink); font-size: 14px; }
  .banner--wide .site-url { color: var(--white); font-size: 13px; }
  .banner--wide .headline { left: 6px; width: 132px; top: 6px; font-size: 14px; line-height: 16.5px; }
  .banner--wide .slogan { left: 2px; width: 140px; top: 77px; font-size: 12px; line-height: 15.5px; }

  .slide-label { position: absolute; color: var(--label-red); font-size: 15px; font-weight: 400; }
</style>
</head>
<body>
<main class="stage">

  <section class="banner banner--tall" style="left:25px;top:37px;">
    <div class="media-panel" style="left:5px;top:4px;width:150px;height:215px;">
      <p class="brand-name" style="top:16px;font-size:20px;">The MealWise<br>Plan</p>
      <div class="photo photo--salad" style="top:66px;" role="img" aria-label="Woman eating a fresh salad from a bowl"></div>
    </div>
    <h2 class="headline">Want to loose<br>extra pounds<br>with<br>healthy food?</h2>
    <p class="slogan">Gourmet Meals<br>Direct To Your House</p>
    <div class="price-badge" style="left:14px;top:386px;width:132px;height:132px;" role="img" aria-label="Round seal behind the price ribbon"></div>
    <div class="ribbon" style="left:41px;top:382px;width:78px;">
      <div class="ribbon__intro" style="height:60px;font-size:14px;line-height:18px;">Starting<br>at<br>only</div>
      <div class="ribbon__price" style="height:82px;font-size:36px;padding-top:14px;">$99</div>
    </div>
    <a class="cta" style="left:8px;top:542px;width:145px;height:30px;font-size:15px;">Click here
      <svg width="20" height="20" viewBox="0 0 20 20" aria-hidden="true"><circle cx="10" cy="10" r="9" fill="#e8e8e8" stroke="#6b6b6b"/><path d="M8 5l5 5-5 5" fill="none" stroke="#555" stroke-width="2.4"/></svg>
    </a>
    <p class="site-url">brightplatekitchen.com</p>
  </section>

  <section class="banner banner--tall" style="left:194px;top:37px;">
    <div class="media-panel" style="left:5px;top:4px;width:150px;height:215px;">
      <p class="brand-name" style="top:16px;font-size:20px;">The MealWise<br>Plan</p>
      <div class="photo photo--waist" style="top:66px;" role="img" aria-label="Slim waist being measured with a tape measure"></div>
    </div>
    <h2 class="headline">Want to loose<br>extra pounds<br>with<br>healthy food?</h2>
    <p class="slogan">Gourmet Meals<br>Direct To Your House</p>
    <div class="price-badge" style="left:14px;top:386px;width:132px;height:132px;" role="img" aria-label="Round seal behind the price ribbon"></div>
    <div class="ribbon" style="left:41px;top:382px;width:78px;">
      <div class="ribbon__intro" style="height:60px;font-size:14px;line-height:18px;">Starting<br>at<br>only</div>
      <div class="ribbon__price" style="height:82px;font-size:36px;padding-top:14px;">$99</div>
    </div>
    <a class="cta" style="left:8px;top:542px;width:145px;height:30px;font-size:15px;">Click here
      <svg width="20" height="20" viewBox="0 0 20 20" aria-hidden="true"><circle cx="10" cy="10" r="9" fill="#e8e8e8" stroke="#6b6b6b"/><path d="M8 5l5 5-5 5" fill="none" stroke="#555" stroke-width="2.4"/></svg>
    </a>
    <p class="site-url">brightplatekitchen.com</p>
  </section>

  <p class="slide-label" style="left:81px;top:645px;">Slide 1</p>
  <p class="slide-label" style="left:250px;top:645px;">Slide 2</p>

  <section class="banner banner--wide" style="left:372px;top:67px;">
    <h2 class="headline">Want to loose<br>extra pounds<br>with<br>healthy food?</h2>
    <p class="slogan">Gourmet Meals<br>Direct To Your House</p>
    <div class="price-badge" style="left:22px;top:117px;width:100px;height:100px;" role="img" aria-label="Round seal behind the price ribbon"></div>
    <div class="ribbon" style="left:41px;top:116px;width:62px;">
      <div class="ribbon__intro" style="height:46px;font-size:11.5px;line-height:14px;">Starting<br>at<br>only</div>
      <div class="ribbon__price" style="height:56px;font-size:29px;padding-top:5px;">$99</div>
    </div>
    <a class="cta" style="left:11px;top:222px;width:125px;height:24px;font-size:13px;gap:6px;">Click here
      <svg width="17" height="17" viewBox="0 0 20 20" aria-hidden="true"><circle cx="10" cy="10" r="9" fill="#e8e8e8" stroke="#6b6b6b"/><path d="M8 5l5 5-5 5" fill="none" stroke="#555" stroke-width="2.4"/></svg>
    </a>
    <div class="media-panel" style="left:144px;top:5px;width:154px;height:216px;">
      <p class="brand-name" style="top:16px;font-size:19px;">The MealWise<br>Plan</p>
      <div class="photo photo--salad" style="top:64px;" role="img" aria-label="Woman eating a fresh salad from a bowl"></div>
    </div>
    <p class="site-url" style="left:144px;width:154px;top:226px;">brightplatekitchen.com</p>
  </section>

  <p class="slide-label" style="left:499px;top:322px;">Slide 1</p>

  <section class="banner banner--wide" style="left:372px;top:348px;">
    <h2 class="headline">Want to loose<br>extra pounds<br>with<br>healthy food?</h2>
    <p class="slogan">Gourmet Meals<br>Direct To Your House</p>
    <div class="price-badge" style="left:22px;top:117px;width:100px;height:100px;" role="img" aria-label="Round seal behind the price ribbon"></div>
    <div class="ribbon" style="left:41px;top:116px;width:62px;">
      <div class="ribbon__intro" style="height:46px;font-size:11.5px;line-height:14px;">Starting<br>at<br>only</div>
      <div class="ribbon__price" style="height:56px;font-size:29px;padding-top:5px;">$99</div>
    </div>
    <a class="cta" style="left:11px;top:222px;width:125px;height:24px;font-size:13px;gap:6px;">Click here
      <svg width="17" height="17" viewBox="0 0 20 20" aria-hidden="true"><circle cx="10" cy="10" r="9" fill="#e8e8e8" stroke="#6b6b6b"/><path d="M8 5l5 5-5 5" fill="none" stroke="#555" stroke-width="2.4"/></svg>
    </a>
    <div class="media-panel" style="left:144px;top:5px;width:154px;height:216px;">
      <p class="brand-name" style="top:16px;font-size:19px;">The MealWise<br>Plan</p>
      <div class="photo photo--waist" style="top:64px;" role="img" aria-label="Slim waist being measured with a tape measure"></div>
    </div>
    <p class="site-url" style="left:144px;width:154px;top:226px;">brightplatekitchen.com</p>
  </section>

  <p class="slide-label" style="left:499px;top:604px;">Slide 2</p>

</main>
</body>
</html>
```